RW Skyline Imaging Web Site design

I am looking for a responsive single page website deign for rwskylineimages.example. This is a drone based aerial photography and cinematography business. It should have an about us section, a services section that contains photograph service, Video footage, and Aerial mapping all under the services section, a pricing section, and then a contact page for customers to contact us.

Coding

Coded - Design and coding required

Number of Pages Required

1 page

Font styles to use
Sans Serif

Colors

Designer to choose colors to be used in the design.

Requirements
Must have
• Responsive design. About us section, services section, pricing section under the services links, and contact us section, that links to a submission page where they can send Name, address, email, and comments on what they are interested in.
• See flyquad7x.example - looking for similar design.
Should not have
• clutter, or too busy design

```html
<!DOCTYPE html>
<html lang="en">
<head>
<meta charset="utf-8">
<title>RW Skyline Imaging</title>
<link rel="stylesheet" href="https://fonts.googleapis.com/css2?family=Lato:wght@300;400;700;900&display=swap">
<style>
:root{
  --orange:#f6961f;
  --orange-dark:#e5861a;
  --ink:#222;
  --grey:#555;
  --light:#f5f5f5;
  --white:#fff;
  --black:#000;
  --card:#222;
  --card-head:#555;
  --card-price:#3d3d3d;
  --card-item:#e9e9e9;
}
*{margin:0;padding:0;box-sizing:border-box}
html,body{width:1200px;height:4196px;overflow:hidden}
body{position:relative;background:var(--light);font-family:'Lato',sans-serif;color:var(--ink)}
.abs{position:absolute}
/* header */
.site-header{left:0;top:0;width:1200px;height:129px;background:var(--white)}
.brand{left:0;width:1200px;top:36px;text-align:center}
.brand-mark{display:inline-block;width:26px;height:26px;border-radius:50%;background:var(--orange)}
.brand-name{display:block;margin-top:10px;font-size:15px;letter-spacing:6px;color:var(--ink)}
.menu-toggle{left:1066px;top:60px;width:18px;height:14px}
/* hero */
.hero{left:0;top:129px;width:1200px;height:612px;background:linear-gradient(180deg,#6d8da3 0%,#8aa0ad 18%,#5a6268 40%,#6b6257 70%,#544a40 100%)}
.hero-title{left:0;width:1200px;top:410px;text-align:center;color:var(--white);font-size:30px;font-weight:700;letter-spacing:1px}
.hero-sub{left:330px;width:540px;top:452px;text-align:center;color:var(--white);font-size:15px;line-height:20px}
.btn-outline{display:block;border:2px solid currentColor;border-radius:6px;text-align:center;font-size:14px}
.hero-btn{left:527px;top:513px;width:138px;height:38px;line-height:34px;color:var(--white)}
.slider-dots{left:566px;top:764px;display:flex;gap:10px}
.slider-dots span{width:15px;height:15px;border:2px solid #888;border-radius:50%}
.slider-dots span:first-child{background:#bbb}
/* section titles */
.section-title{left:0;width:1200px;text-align:center}
.section-title h2{font-size:30px;font-weight:700;letter-spacing:2px;color:var(--ink)}
.section-title p{display:inline-flex;align-items:center;gap:10px;font-size:13px;margin-top:2px}
.section-title p::before,.section-title p::after{content:"";width:58px;height:2px;background:var(--ink)}
.section-title.light h2,.section-title.light p{color:var(--white)}
/* about */
.about-text{left:120px;top:905px;width:475px;font-size:15px;line-height:20px;color:var(--grey)}
.about-text p+p{margin-top:18px}
.about-btn{left:120px;top:1087px;width:137px;height:36px;line-height:32px;color:#333;border-color:#555}
.showreel{left:615px;top:909px;width:462px;height:274px;background:linear-gradient(135deg,#8a9099,#4d5258 55%,#2f3236)}
.play{left:818px;top:1022px}
.drone-art{left:0;top:1133px;width:168px;height:140px;background:radial-gradient(ellipse at center,#8b8e93 0%,#c9cbcd 45%,rgba(245,245,245,0) 70%)}
/* services */
.services{left:0;top:1278px;width:1200px;height:593px;background:var(--orange)}
.service{width:300px;text-align:center;color:var(--white)}
.service svg{display:block;margin:0 auto}
.service h3{font-size:15px;font-weight:700;margin-top:12px}
.service p{font-size:13px;line-height:19px;margin-top:10px;padding:0 40px}
.service a{display:block;font-size:13px;margin-top:10px;color:var(--white);text-decoration:none}
.view-btn{left:534px;top:1755px;width:137px;height:36px;line-height:32px;color:var(--white)}
/* gallery */
.filters{left:0;width:1200px;top:2010px;text-align:center;font-size:12px;letter-spacing:1px;color:#555}
.filters span{padding:0 10px;border-left:1px solid #999}
.filters span:first-child{border-left:0}
.photo{background:linear-gradient(160deg,#8a8f90,#55606a)}
.photo.sea{background:linear-gradient(160deg,#3b6a8a,#1f4760)}
.photo.coast{background:linear-gradient(160deg,#8b7a60,#4a6a70)}
.photo.city{background:linear-gradient(180deg,#9aa8b2,#56606a)}
.gallery-btn{left:534px;top:2775px;width:137px;height:34px;line-height:30px;color:#333;border-color:#555}
/* rates */
.rates{left:0;top:3012px;width:1200px;height:557px;background:var(--orange)}
.plan{width:266px;height:430px;top:3066px;background:var(--card);padding:10px}
.plan-head{height:54px;line-height:54px;background:var(--card-head);color:var(--white);text-align:center;font-size:15px;font-weight:700}
.plan-price{height:70px;line-height:70px;margin-top:3px;background:var(--card-price);color:var(--white);text-align:center;font-size:32px;font-weight:700}
.plan ul{list-style:none;margin-top:8px}
.plan li{height:40px;line-height:40px;margin-bottom:3px;background:var(--card-item);text-align:center;font-size:15px;font-weight:700;color:#333}
.plan-buy{height:48px;line-height:48px;margin-top:5px;background:var(--card-head);color:var(--white);text-align:center;font-size:20px;font-weight:900}
/* newsletter */
.news-title{left:0;width:1200px;top:3648px;text-align:center;font-size:23px;font-weight:700;letter-spacing:1px}
.news-sub{left:0;width:1200px;top:3679px;text-align:center;font-size:13px;letter-spacing:2px}
.news-input{left:344px;top:3730px;width:392px;height:22px;border:1px solid #ccc;background:var(--white);font-size:10px;line-height:20px;padding-left:8px;color:#888}
.news-btn{left:738px;top:3730px;width:90px;height:22px;background:var(--orange);color:var(--white);font-size:12px;font-weight:700;line-height:22px;text-align:center;letter-spacing:1px}
/* footer */
.site-footer{left:0;top:3840px;width:1200px;height:356px;background:var(--black);color:var(--white)}
.foot-h{top:3910px;font-size:14px;font-weight:700}
.foot-h::after{content:"";display:block;width:52px;height:3px;background:var(--white);margin-top:5px}
.foot-about{left:120px;top:3960px;width:180px;font-size:14px;font-weight:700;line-height:20px}
.foot-links{left:361px;top:3956px;list-style:none;font-size:14px;font-weight:700;line-height:24px}
.foot-contact{left:534px;top:3956px;font-size:13px;font-weight:700;line-height:24px}
.foot-contact td{vertical-align:top;padding-right:8px}
.field{background:#222;color:#bbb;font-size:12px;padding:4px 8px;border:1px solid #333}
.send{left:946px;top:4071px;width:134px;height:30px;background:var(--orange);border-radius:4px;text-align:center;line-height:30px;font-size:12px;font-weight:700}
.copyright{left:120px;top:4158px;font-size:14px;font-weight:700}
.social{left:910px;top:4159px;display:flex;gap:24px}
.social span{width:14px;height:14px;background:var(--white)}
</style>
</head>
<body>

<header class="abs site-header">
  <div class="abs brand"><span class="brand-mark"></span><span class="brand-name">RW Skyline Imaging</span></div>
  <svg class="abs menu-toggle" viewBox="0 0 18 14"><rect y="0" width="18" height="2.5" fill="#f6961f"/><rect y="5.7" width="18" height="2.5" fill="#f6961f"/><rect y="11.5" width="18" height="2.5" fill="#f6961f"/></svg>
</header>

<section class="abs hero" role="img" aria-label="Aerial view of a city skyline under a blue sky"></section>
<h1 class="abs hero-title">AERIAL PHOTOGRAPHY</h1>
<p class="abs hero-sub">Aerial Photography For Real Estate Architectural Sports Commercial Advertising And Environmental Professionals</p>
<a class="abs btn-outline hero-btn">Read More</a>
<div class="abs slider-dots"><span></span><span></span><span></span></div>

<div class="abs section-title" style="top:805px"><h2>ABOUT US</h2><p>Show Reel</p></div>
<div class="abs about-text">
  <p>RW Skyline Imaging provides services for Real Estate, Architectural, Sports Commercial, Advertising, Environmental professionalsor personal aerial photo sessions.</p>
  <p>We serve San Diego South Riverside Orange and Los Angeles counties with the best aerial photography around.All photographs are copyright protected and the property of RW Skyline Imaging</p>
</div>
<a class="abs btn-outline about-btn">Read More</a>
<div class="abs showreel" role="img" aria-label="Show reel video still of downtown towers from above"></div>
<svg class="abs play" width="56" height="56" viewBox="0 0 56 56"><circle cx="28" cy="28" r="26" fill="rgba(0,0,0,.55)" stroke="#fff" stroke-width="2"/><path d="M22 17 L40 28 L22 39 Z" fill="#fff"/></svg>
<div class="abs drone-art" role="img" aria-label="Quadcopter drone illustration"></div>

<section class="abs services"></section>
<div class="abs section-title light" style="top:1350px"><h2>OUR SERVICES</h2></div>
<p class="abs" style="left:0;width:1200px;top:1389px;text-align:center;color:#fff;font-size:14px;line-height:19px">Lorem Ipsum is simply dummy text of the printing<br>and typesetting industry.</p>

<div class="abs service" style="left:99px;top:1505px">
  <svg width="58" height="58" viewBox="0 0 58 58" fill="none" stroke="#fff" stroke-width="3"><circle cx="12" cy="12" r="8"/><circle cx="46" cy="12" r="8"/><circle cx="12" cy="46" r="8"/><circle cx="46" cy="46" r="8"/><path d="M18 18 L40 40 M40 18 L18 40"/><rect x="22" y="22" width="14" height="14" fill="#fff"/></svg>
  <h3>PHOTOGRAPHY</h3>
  <p>Lorem Ipsum is simply a dummy text of the printing purpose and typesettingindustry.</p>
  <a>Read More &#10148;</a>
</div>
<div class="abs service" style="left:449px;top:1505px">
  <svg width="58" height="58" viewBox="0 0 58 58" fill="none" stroke="#fff" stroke-width="3"><rect x="4" y="8" width="50" height="42" rx="3"/><path d="M14 8 V50 M44 8 V50"/><path d="M24 20 L36 29 L24 38 Z" fill="#fff"/></svg>
  <h3>VIDEOGRAPHY</h3>
  <p>Lorem Ipsum is simply a dummy text of the printing purpose and typesettingindustry.</p>
  <a>Read More &#10148;</a>
</div>
<div class="abs service" style="left:762px;top:1505px">
  <svg width="58" height="58" viewBox="0 0 58 58" fill="none" stroke="#fff" stroke-width="3"><path d="M4 52 L14 30 L22 34 L36 34 L44 30 L54 52 Z"/><path d="M29 40 C20 28 20 22 20 18 A9 9 0 0 1 38 18 C38 22 38 28 29 40 Z"/><circle cx="29" cy="18" r="3"/></svg>
  <h3>3D MAPPING</h3>
  <p>Lorem Ipsum is simply a dummy text of the printing purpose and typesettingindustry.</p>
  <a>Read More &#10148;</a>
</div>
<a class="abs btn-outline view-btn">View More</a>

<div class="abs section-title" style="top:1927px"><h2>PHOTO GALLERY</h2><p>Areal Shots</p></div>
<div class="abs filters"><span>ALL</span><span>SPORTS</span><span>REAL ESTATE</span><span>ARIEL SHOTS</span><span>VIDEO</span><span>OTHER</span></div>

<div class="abs photo coast" style="left:120px;top:2070px;width:308px;height:263px" role="img" aria-label="Aerial shot of a seaside house and rocks"></div>
<div class="abs photo sea" style="left:120px;top:2350px;width:308px;height:265px" role="img" aria-label="Aerial shot of waves along a beach"></div>
<div class="abs photo city" style="left:120px;top:2632px;width:308px;height:173px" role="img" aria-label="Aerial shot of a city skyline"></div>
<div class="abs photo sea" style="left:445px;top:2070px;width:307px;height:173px" role="img" aria-label="Aerial shot of surfers in the ocean"></div>
<div class="abs photo sea" style="left:445px;top:2260px;width:307px;height:263px" role="img" aria-label="Aerial shot of rowers in a yellow canoe"></div>
<div class="abs photo sea" style="left:445px;top:2540px;width:307px;height:173px" role="img" aria-label="Aerial shot of boat wakes on water"></div>
<div class="abs photo coast" style="left:772px;top:2070px;width:305px;height:263px" role="img" aria-label="Aerial shot of a coastal cliff and railway"></div>
<div class="abs photo coast" style="left:772px;top:2350px;width:305px;height:265px" role="img" aria-label="Aerial shot of a sandy beach and surf"></div>
<div class="abs photo city" style="left:772px;top:2632px;width:305px;height:173px" role="img" aria-label="Aerial shot of a lake in a neighborhood"></div>
<a class="abs btn-outline gallery-btn" style="background:var(--light)">View More</a>

<div class="abs section-title" style="top:2914px"><h2>OUR RATES</h2><p>Areal Shots</p></div>
<section class="abs rates"></section>
<div class="abs plan" style="left:182px">
  <div class="plan-head">STANDARD</div><div class="plan-price">$800.00</div>
  <ul><li>lorem ipsum 1</li><li>lorem ipsum 2</li><li>lorem ipsum 3</li><li>lorem ipsum 4</li><li>lorem ipsum 5</li></ul>
  <div class="plan-buy">PURCHASE</div>
</div>
<div class="abs plan" style="left:459px">
  <div class="plan-head">PREMIUM</div><div class="plan-price">$1200.00</div>
  <ul><li>lorem ipsum 1</li><li>lorem ipsum 2</li><li>lorem ipsum 3</li><li>lorem ipsum 4</li><li>lorem ipsum 5</li></ul>
  <div class="plan-buy">PURCHASE</div>
</div>
<div class="abs plan" style="left:742px">
  <div class="plan-head">BUSINESS</div><div class="plan-price">$1200.00</div>
  <ul><li>lorem ipsum 1</li><li>lorem ipsum 2</li><li>lorem ipsum 3</li><li>lorem ipsum 4</li><li>lorem ipsum 5</li></ul>
  <div class="plan-buy">PURCHASE</div>
</div>

<h2 class="abs news-title">SUBSCRIBE TO OUR NEWSLETTER</h2>
<p class="abs news-sub">TO RECEIVE THE LATEST NEWS &amp; UPDATE</p>
<div class="abs news-input">Your Email</div>
<div class="abs news-btn">SUBMIT</div>

<footer class="abs site-footer"></footer>
<h4 class="abs foot-h" style="left:120px">ABOUT US</h4>
<p class="abs foot-about">Lorem Ipsum is simply dummy text of the prin ting and typesetting indu stry. Lorem Ipsum<br><span style="display:inline-block;margin-top:6px">Read More.. &#9673;</span></p>
<h4 class="abs foot-h" style="left:361px">QUICK LINK</h4>
<ul class="abs foot-links"><li>About</li><li>Services</li><li>Blog</li><li>Price</li><li>Testimonials</li></ul>
<h4 class="abs foot-h" style="left:534px">CONTACT US</h4>
<table class="abs foot-contact">
  <tr><td>Address</td><td>: 123th Street,<br>&nbsp;&nbsp;City</td></tr>
  <tr><td>Phone</td><td>: +1 555 010 2040</td></tr>
  <tr><td>Fax</td><td>: +1 555 010 2041</td></tr>
  <tr><td>E-mail</td><td>: info@rwskylineimages.example</td></tr>
</table>
<h4 class="abs foot-h" style="left:806px">QUICK CONTACT</h4>
<div class="abs field" style="left:806px;top:3958px;width:134px;height:24px">Name</div>
<div class="abs field" style="left:946px;top:3958px;width:134px;height:24px">Phone</div>
<div class="abs field" style="left:806px;top:3992px;width:274px;height:60px">Message</div>
<div class="abs send">SEND</div>
<p class="abs copyright">Copyright 2017 RW Skyline Imaging LLC, All Rights Reserved.</p>
<div class="abs social"><span></span><span></span><span></span><span></span><span></span></div>

</body>
</html>
```